Consulting group
Business cards and stationary
Use same font as used in my logo
I think it is Swiss721?
Simple
Damon Fairley
President
417 W. Marlow Avenue, Apt 118 Ann Arbor, MI 48177
Damon@DamonFairley.com
www.TheCopperLantern.com
Looking for envelope, letterhead, and business card.
the logo? if you want to try putting a quote on it: "“The worst thing that can happen to a good cause is, not to be skillfully attacked, but to be ineptly defended.” - Corvelle. Not sure if I will like the quote on there or not.

```html
<!DOCTYPE html>
<html lang="en">
<head>
<meta charset="utf-8">
<title>The Copper Lantern – Business Card</title>
<link rel="stylesheet" href="https://fonts.googleapis.com/css2?family=Arimo:wght@400;700&display=swap">
<style>
  :root {
    --brand-red: #e3262b;
    --ink: #1d1d1d;
    --ink-soft: #555555;
    --card-dark: #1e1e1e;
    --paper: #ffffff;
    --backdrop: #d9d9d9;
    --quote-text: #e8e8e8;
  }
  * { margin: 0; padding: 0; box-sizing: border-box; }
  html, body {
    width: 1200px; height: 901px; overflow: hidden;
    background: var(--backdrop);
    font-family: "Arimo", Arial, sans-serif;
  }
  .canvas {
    position: relative; width: 1200px; height: 901px;
  }
  .card {
    position: absolute; left: 337px;
    width: 525px; height: 300px;
    overflow: hidden;
    box-shadow: 0 6px 18px rgba(0,0,0,.18);
  }
  /* Back of card */
  .card-back { top: 100px; background: var(--card-dark); }
  .card-back .brand-name {
    position: absolute; top: 92px; left: 0; right: 0;
    text-align: center;
    color: var(--brand-red); font-weight: 700; font-size: 40px; letter-spacing: -0.5px;
  }
  .card-back .quote {
    position: absolute; top: 212px; left: 40px; right: 40px;
    text-align: center; color: var(--quote-text);
    font-size: 13px; line-height: 1.45;
  }
  /* Front of card */
  .card-front { top: 500px; background: var(--paper); }
  .logo-lockup {
    position: absolute; top: 34px; left: 34px;
    display: flex; align-items: flex-start; gap: 12px;
  }
  .logo-square { width: 40px; height: 40px; background: var(--brand-red); flex: none; }
  .logo-name {
    color: var(--ink); font-weight: 700; font-size: 24px; line-height: 1.02; width: 110px;
  }
  .contact {
    position: absolute; top: 112px; left: 270px; width: 240px;
    color: var(--ink);
  }
  .contact .person { font-weight: 700; font-size: 17px; }
  .contact .title { color: var(--ink-soft); font-size: 12px; margin-top: 3px; margin-bottom: 12px; }
  .contact .row {
    display: flex; align-items: flex-start; gap: 8px;
    font-size: 11px; line-height: 1.4; margin-bottom: 4px;
  }
  .contact .row svg { flex: none; margin-top: 2px; }
  .web-band {
    position: absolute; left: 0; right: 0; bottom: 22px; height: 30px;
    background: var(--brand-red);
    border-radius: 15px 0 0 15px; margin-left: 30px;
    display: flex; align-items: center; padding-left: 22px;
    color: var(--paper); font-weight: 700; font-size: 14px;
  }
</style>
</head>
<body>
<main class="canvas">
  <section class="card card-back" aria-label="Card back">
    <div class="brand-name">The Copper Lantern</div>
    <p class="quote">“The worst thing that can happen to a good cause is, not to be skillfully attacked, but to be ineptly defended.” - Corvelle</p>
  </section>

  <section class="card card-front" aria-label="Card front">
    <div class="logo-lockup">
      <div class="logo-square"></div>
      <div class="logo-name">The Copper Lantern</div>
    </div>

    <div class="contact">
      <div class="person">Damon Fairley</div>
      <div class="title">President</div>
      <div class="row">
        <svg width="10" height="12" viewBox="0 0 10 12"><path d="M5 0a4 4 0 0 0-4 4c0 3 4 8 4 8s4-5 4-8a4 4 0 0 0-4-4zm0 5.5A1.5 1.5 0 1 1 5 2.5a1.5 1.5 0 0 1 0 3z" fill="var(--brand-red)"/></svg>
        <span>417 W. Marlow Avenue, Apt 118<br>Ann Arbor, MI 48177</span>
      </div>
      <div class="row">
        <svg width="10" height="10" viewBox="0 0 10 10"><path d="M2 0h2l1 2.5-1.3 1a6 6 0 0 0 2.8 2.8l1-1.3L10 6v2a2 2 0 0 1-2 2A8 8 0 0 1 0 2a2 2 0 0 1 2-2z" fill="var(--brand-red)"/></svg>
        <span>734.555.0186</span>
      </div>
      <div class="row">
        <svg width="10" height="10" viewBox="0 0 10 10"><rect x="0" y="3" width="10" height="6" fill="var(--brand-red)"/><rect x="2" y="0" width="6" height="3" fill="none" stroke="var(--brand-red)"/></svg>
        <span>734.555.0142</span>
      </div>
      <div class="row">
        <svg width="11" height="8" viewBox="0 0 11 8"><rect x=".5" y=".5" width="10" height="7" fill="none" stroke="var(--brand-red)"/><path d="M.5.5l5 4 5-4" fill="none" stroke="var(--brand-red)"/></svg>
        <span>Damon@DamonFairley.com</span>
      </div>
    </div>

    <div class="web-band">www.TheCopperLantern.com</div>
  </section>
</main>
</body>
</html>
```